Business card for a Exhibition booth fabrication company

Hi. My company would like to change our corporate name card. We are an events and Exhibition stand builder company. We would like our corporate name card to resonate what we do. I need someone to create something unique that relates to the industry that I am in. The graphic designer should be creative to incorporate the elements of my industry and try to blend in well in the design of the card. Our aim is to ensure that we are unique and our card can look different from our competitors.
Updates

The decision maker was very busy and didnt had time to make this decision

Target Market(s)

Marketing and events manager from all companies

Contact Information for Business Card

The business card should have the following details:
Name
Job Title
Email
Website

Colors

Designer to choose colors to be used in the design.

Requirements
Must have
• The card must be look something that is relevant to the service that I am providing. My website is: www.velmora-buildworks.example
• You can see my website to get more information on what service that I am doing
Nice to have
• On the back of my card, I would like to have a globe image with the incorporation of my company logo. This is to indicate that my services can be done in any part of the world.

```html
<!DOCTYPE html>
<html lang="en">
<head>
<meta charset="utf-8">
<title>Velmora Buildworks – Business Card</title>
<link rel="stylesheet" href="https://fonts.googleapis.com/css2?family=Montserrat:wght@400;500;600&family=Arimo:wght@400&display=swap">
<style>
  :root {
    --page-bg: #ebebeb;
    --card-white: #ffffff;
    --brand-red: #d71f27;
    --ink: #2a2a2a;
    --grey-text: #6a6a6a;
    --globe-light: #e4e4e4;
    --globe-dark: #9a9a9a;
    --photo-pink: #ecd2d6;
    --photo-lilac: #d9d6ef;
    --photo-cream: #f1e6e2;
    --divider: #7a7a7a;
  }
  * { box-sizing: border-box; margin: 0; padding: 0; }
  html, body { width: 1200px; height: 1200px; overflow: hidden; }
  body {
    background: var(--page-bg);
    font-family: "Arimo", Arial, sans-serif;
    color: var(--ink);
    position: relative;
  }
  .card {
    position: absolute;
    left: 150px;
    width: 900px;
    height: 514px;
    background: var(--card-white);
    overflow: hidden;
    box-shadow: 0 10px 28px rgba(0,0,0,0.12);
  }
  .card--front { top: 50px; }
  .card--back { top: 630px; }

  /* Front */
  .globe {
    position: absolute;
    left: 200px;
    top: 90px;
    width: 560px;
    height: 560px;
    border-radius: 50%;
    background: radial-gradient(circle at 55% 35%, var(--globe-light) 0%, #c4c4c4 55%, var(--globe-dark) 100%);
    opacity: 0.75;
  }
  .brand {
    position: absolute;
    left: 0; right: 0;
    top: 210px;
    display: flex;
    align-items: center;
    justify-content: center;
    gap: 18px;
  }
  .brand__mark {
    width: 54px; height: 54px;
    border-radius: 50%;
    background: var(--brand-red);
  }
  .brand__name {
    font-family: "Montserrat", Arial, sans-serif;
    font-weight: 500;
    font-size: 34px;
    letter-spacing: 8px;
    color: var(--ink);
    white-space: nowrap;
  }
  .front-band {
    position: absolute;
    left: 0; right: 0; bottom: 0;
    height: 44px;
    background: var(--brand-red);
    display: flex;
    align-items: center;
    padding-left: 60px;
  }
  .front-band__url {
    color: var(--card-white);
    font-size: 20px;
    letter-spacing: 0.5px;
  }

  /* Back */
  .showroom-photo {
    position: absolute;
    left: 0; top: 0;
    width: 900px; height: 340px;
    background: linear-gradient(110deg, var(--photo-pink) 0%, var(--photo-cream) 40%, #e6d3df 65%, var(--photo-lilac) 100%);
  }
  .back-brand {
    position: absolute;
    left: 60px; top: 80px;
    width: 440px;
  }
  .back-brand__row { display: flex; align-items: center; gap: 12px; }
  .back-brand__mark {
    width: 36px; height: 36px; border-radius: 50%;
    background: var(--brand-red);
    flex: none;
  }
  .back-brand__name {
    font-family: "Montserrat", Arial, sans-serif;
    font-weight: 500;
    font-size: 20px;
    letter-spacing: 4px;
    color: var(--ink);
    white-space: nowrap;
  }
  .back-brand__tagline {
    margin-top: 10px;
    font-size: 11px;
    letter-spacing: 0.4px;
    color: var(--ink);
    text-transform: uppercase;
    white-space: nowrap;
  }
  .back-divider {
    position: absolute;
    left: 515px; top: 60px;
    width: 2px; height: 200px;
    background: var(--divider);
  }
  .contact {
    position: absolute;
    left: 535px; top: 70px;
    display: flex; flex-direction: column; gap: 18px;
  }
  .contact__line { display: flex; align-items: center; gap: 12px; color: var(--ink); }
  .contact__icon { width: 30px; height: 30px; flex: none; }
  .contact__phones { display: flex; flex-direction: column; gap: 8px; font-size: 19px; }
  .phone { display: flex; align-items: center; gap: 10px; white-space: nowrap; }
  .flag { width: 28px; height: 18px; display: block; flex: none; }
  .flag--sg { background: linear-gradient(var(--brand-red) 50%, #fff 50%); box-shadow: 0 0 0 1px #ccc; }
  .flag--qa { background: linear-gradient(90deg, #fff 30%, #8a1538 30%); box-shadow: 0 0 0 1px #ccc; }
  .contact__email { font-size: 18px; white-space: nowrap; }

  .services {
    position: absolute;
    left: 0; right: 0; bottom: 0;
    height: 174px;
    display: flex;
    justify-content: space-around;
    align-items: flex-start;
    padding: 40px 30px 0;
  }
  .service { width: 150px; display: flex; flex-direction: column; align-items: center; gap: 12px; }
  .service__icon { width: 56px; height: 56px; background: var(--brand-red); border-radius: 4px; }
  .service__label { font-size: 12px; color: var(--grey-text); text-align: center; line-height: 1.3; }
</style>
</head>
<body>

<section class="card card--front" aria-label="Business card front">
  <div class="globe" role="img" aria-label="Grey world map globe"></div>
  <div class="brand">
    <span class="brand__mark"></span>
    <span class="brand__name">VELMORA BUILDWORKS</span>
  </div>
  <div class="front-band">
    <span class="front-band__url">www.velmora-buildworks.example</span>
  </div>
</section>

<section class="card card--back" aria-label="Business card back">
  <div class="showroom-photo" role="img" aria-label="Faded photo of an exhibition stand interior"></div>

  <div class="back-brand">
    <div class="back-brand__row">
      <span class="back-brand__mark"></span>
      <span class="back-brand__name">VELMORA BUILDWORKS</span>
    </div>
    <p class="back-brand__tagline">Events and Exhibition Stand Builder Company</p>
  </div>

  <div class="back-divider"></div>

  <div class="contact">
    <div class="contact__line">
      <svg class="contact__icon" viewBox="0 0 34 34" aria-hidden="true">
        <rect x="9" y="3" width="16" height="28" rx="3" fill="none" stroke="var(--brand-red)" stroke-width="2"/>
        <line x1="15" y1="27" x2="19" y2="27" stroke="var(--brand-red)" stroke-width="2"/>
      </svg>
      <div class="contact__phones">
        <div class="phone"><span class="flag flag--sg"></span><span>+65 9000 0142</span></div>
        <div class="phone"><span class="flag flag--qa"></span><span>+974 7000 0287</span></div>
      </div>
    </div>
    <div class="contact__line">
      <svg class="contact__icon" viewBox="0 0 34 34" aria-hidden="true">
        <rect x="3" y="8" width="28" height="18" fill="none" stroke="var(--brand-red)" stroke-width="2"/>
        <polyline points="3,8 17,19 31,8" fill="none" stroke="var(--brand-red)" stroke-width="2"/>
      </svg>
      <span class="contact__email">info@velmora-buildworks.example</span>
    </div>
  </div>

  <div class="services">
    <div class="service"><span class="service__icon" role="img" aria-label="Consultation icon"></span><span class="service__label">Exhibition Consultation</span></div>
    <div class="service"><span class="service__icon" role="img" aria-label="Booth design icon"></span><span class="service__label">Exhibition Booth Design Concept</span></div>
    <div class="service"><span class="service__icon" role="img" aria-label="Construction icon"></span><span class="service__label">Exhibition Booth Construction</span></div>
    <div class="service"><span class="service__icon" role="img" aria-label="Project management icon"></span><span class="service__label">Project Management</span></div>
    <div class="service"><span class="service__icon" role="img" aria-label="Installation icon"></span><span class="service__label">Installation &amp; Dismantling</span></div>
  </div>
</section>

</body>
</html>
```